SipNOW Business Cards

Hi designers!

Here's some background on our start-up and this project:

SipNOW is a website that will allow users to order alcohol from nearby liquor stores and have it delivered to their homes in minutes. We are really excited to work on creating the best online, alcohol purchasing experience for the users.

So why SipNOW? We like to think of ourselves as that great friend who will get alcohol for you because he happens to have a car. We help you drink in with your friends, family, or guests. Our site will target students and young professionals (of drinking age) who are comfortable buying things online or through apps. We don't see this service as a luxury, VIP, or niche service in the least; instead, we think of us as a relaxed, service-driven start-up that believes in simple design and transparent .

Now, we want a business card that incorporates our newly acquired logo design and some complimenting colors and fonts. Feel free to do it single or double sided, although I'm a sucker for double...

If you happen to have any questions, want to throw some ideas around, or just want some feedback- email me at marco@sipnow.example.

Marco Tessin
Founder

Industry/Entity Type

Business

Requirements
Must have
• Name, Position, Email, Cell-phone

No address, no fax, no land-line.

```html
<!DOCTYPE html>
<html lang="en">
<head>
<meta charset="utf-8">
<title>SipNOW Business Card</title>
<link href="https://fonts.googleapis.com/css2?family=Bebas+Neue&family=Oswald:wght@500;600&family=PT+Sans+Narrow:wght@400;700&family=Nunito:wght@800&display=swap" rel="stylesheet">
<style>
  :root {
    --stage: #2c2c2a;
    --card: #fef6e1;
    --ink: #1e1c1b;
    --amber: #f9c11c;
    --amber-deep: #f3a91a;
    --label: #e4e4e4;
    --white: #ffffff;
  }
  * { margin: 0; padding: 0; box-sizing: border-box; }
  html, body { width: 1200px; height: 1000px; overflow: hidden; }
  body { background: var(--stage); position: relative; }

  .card {
    position: absolute;
    left: 152px;
    width: 876px;
    height: 453px;
    background: var(--card);
  }
  .card--front { top: 19px; }
  .card--back { top: 528px; }

  .side-label {
    position: absolute;
    left: 1034px;
    font-family: "Bebas Neue", sans-serif;
    font-size: 56px;
    line-height: 1;
    color: var(--label);
    letter-spacing: 1px;
  }
  .side-label--front { top: 424px; }
  .side-label--back { top: 921px; }

  .wordmark {
    position: absolute;
    left: 0; right: 0;
    top: 168px;
    text-align: center;
    font-family: "Nunito", sans-serif;
    font-weight: 800;
    font-size: 100px;
    line-height: 1;
    color: var(--ink);
    letter-spacing: -1px;
  }

  .bottle {
    position: absolute;
    left: 236px;
    top: 129px;
    width: 472px;
    height: 133px;
    background: var(--amber);
    border-radius: 6px 60px 60px 6px;
  }

  .holder-name {
    position: absolute;
    left: 286px;
    top: 118px;
    width: 240px;
    font-family: "Oswald", sans-serif;
    font-weight: 600;
    font-size: 74px;
    line-height: 70px;
    letter-spacing: 9px;
    color: var(--white);
    text-transform: uppercase;
    text-align: center;
  }
  .holder-role {
    position: absolute;
    left: 286px;
    top: 258px;
    width: 240px;
    text-align: center;
    font-family: "Oswald", sans-serif;
    font-weight: 600;
    font-style: italic;
    font-size: 38px;
    line-height: 1;
    letter-spacing: 5px;
    color: var(--amber);
    text-transform: uppercase;
  }
  .contact {
    position: absolute;
    left: 226px;
    top: 308px;
    width: 360px;
    text-align: center;
    font-family: "PT Sans Narrow", sans-serif;
    color: var(--ink);
    line-height: 1;
  }
  .contact__email { font-size: 30px; letter-spacing: 1px; }
  .contact__phone { font-size: 31px; font-weight: 700; margin-top: 2px; letter-spacing: 1px; }
</style>
</head>
<body>
  <section class="card card--front">
    <div class="wordmark">SipNOW</div>
  </section>
  <div class="side-label side-label--front">FRONT</div>

  <section class="card card--back">
    <div class="bottle" role="img" aria-label="Yellow bottle silhouette lying on its side"></div>
    <h1 class="holder-name">Marco<br>Tessin</h1>
    <p class="holder-role">Founder</p>
    <div class="contact">
      <p class="contact__email">marco@sipnow.example</p>
      <p class="contact__phone">(000) 000-0000</p>
    </div>
  </section>
  <div class="side-label side-label--back">BACK</div>
</body>
</html>
```